Business Card Design Project: Classically Trained Singer and Voice Teacher

I am a classically trained singer that performs in Opera and Musical Theater and also teaches private voice lessons in those fields. I am looking for a business card that I can give to casting directors and colleagues, as well as to people who are interested in taking voice lessons from me.

This is sort of like an actors business card so I want my headshot and name to be the main focus.

I was kind of thinking of having the business card be horizontal with my headshot photo on the front taking up roughly half and my information on the same side, and perhaps my name again on the back or some form of my initials. But I am totally open to other options for layout.I would prefer to have a double sided business card, but once again, its not essential.

I am looking for it to look and feel elegant artistic and professional, without looking feminine.

Because of the colors of my headshot I would imagine that it would be predominantly brown and white, but I am totally open to other approaches.feel totally free to crop my headshot so that it fits better into your overall design and layout.

It is highly likely that I will ask the winner of the design to create a flyer for marketing my voice lessons with a similar look.

If you have any questions or clarifications, please feel free to ask.

Target Market(s)

Opera and Musical theater casting directors, colleagues; potential voice lesson students

Industry/Entity Type

Marketing

Requirements
Must have
• These must feature prominently:
- (My Headshot (attached))
- Marlow Keating (my name)

These dont need to be as prominent:
- Baritone
- Private Voice Teacher
- Opera and Musical Theater

Contact Info:
Phone: (555) 347-2816
Email: marlkeat@inboxly.example

Nice to have
• Double sided

```html
<!DOCTYPE html>
<html lang="en">
<head>
<meta charset="utf-8">
<title>Marlow Keating – Business Card</title>
<link rel="stylesheet" href="https://fonts.googleapis.com/css2?family=Mulish:wght@300;400&family=Pinyon+Script&display=swap">
<style>
  :root {
    --card-white: #ffffff;
    --ink: #1a1a1a;
    --ink-soft: #2b2b2b;
    --tan: #c59572;
    --photo-light: #c9c3bc;
    --photo-mid: #8a6a52;
    --photo-dark: #3e2b20;
  }
  html, body {
    margin: 0;
    padding: 0;
    width: 1200px;
    height: 734px;
    overflow: hidden;
    background: var(--card-white);
  }
  .card {
    position: relative;
    width: 1200px;
    height: 734px;
    background: var(--card-white);
    overflow: hidden;
  }
  .headshot {
    position: absolute;
    left: 0;
    top: 0;
    width: 582px;
    height: 734px;
    background:
      radial-gradient(ellipse 55% 45% at 48% 38%, #b89377 0%, rgba(184,147,119,0) 70%),
      linear-gradient(180deg, var(--photo-light) 0%, #9f8676 35%, var(--photo-mid) 65%, var(--photo-dark) 100%);
  }
  .details {
    position: absolute;
    left: 637px;
    top: 70px;
    font-family: "Mulish", "Helvetica Neue", Arial, sans-serif;
    color: var(--ink-soft);
  }
  .roles {
    margin: 0;
    padding: 0;
    list-style: none;
    font-weight: 300;
    font-size: 33px;
    line-height: 42px;
  }
  .phone {
    margin: 14px 0 0;
    font-weight: 300;
    font-size: 66px;
    line-height: 1;
    color: var(--tan);
    letter-spacing: 1px;
  }
  .email {
    margin: 26px 0 0;
    font-weight: 300;
    font-size: 34px;
    color: var(--ink-soft);
  }
  .name {
    position: absolute;
    left: 28px;
    bottom: 48px;
    margin: 0;
    font-family: "Pinyon Script", "Edwardian Script ITC", cursive;
    font-weight: 400;
    font-size: 158px;
    line-height: 1;
    color: var(--ink);
    white-space: nowrap;
  }
</style>
</head>
<body>
  <main class="card">
    <div class="headshot" role="img" aria-label="Headshot portrait of the singer in a tan jacket and striped shirt"></div>
    <section class="details">
      <ul class="roles">
        <li>Baritone</li>
        <li>Private Voice Teacher</li>
        <li>Opera and Musical Theater</li>
      </ul>
      <p class="phone">(555) 347-2816</p>
      <p class="email">marlkeat@inboxly.example</p>
    </section>
    <h1 class="name">Marlow Keating</h1>
  </main>
</body>
</html>
```